The Quiet Meadow - a modern wellness brand

Looking for a modern, simple, and clean website for a virtual consulting firm focused on holistic wellness and sustainable living. Want a strong combo of text and photos (really shitty starts are available for reference on www.thequietmeadowhub.example and www.ginaposlund.example for reference - general idea is in the right direction, was too difficult to work through with the wordpress template and nothing laid out correctly)
Needs include:
- strong home / landing page
- ability to schedule (use calend.ly) on the site
- online shop / purchasing POS integration
- blog
-multiple 'services' pages
- about page
- contact page
(attached brand board images for brand style / reference)
Updates
Want more opportunity for designs and feedback
Target Market(s)
women and gay men aged 30-50
Coding
Coded - Design and coding required
Number of Pages Required
5+ page
Colors
Designer to choose only greyscale colors for use in the design.
Requirements
Must have
- the ability for me to update and manage through wordpress when things like pricing, or services change
Should not have
- complicated anything

```html
<!DOCTYPE html>
<html lang="en">
<head>
<meta charset="utf-8">
<title>The Quiet Meadow</title>
<link rel="stylesheet" href="https://fonts.googleapis.com/css2?family=Jost:wght@300;400&family=Poppins:wght@300;400;500&family=EB+Garamond:ital,wght@0,400;1,400&display=swap">
<style>
:root{
  --charcoal:#2b2b2d;
  --charcoal-soft:#3b3b3e;
  --ink:#1e1e20;
  --text:#6c6c70;
  --mist:#f1f1f2;
  --band:#e5e5e7;
  --white:#ffffff;
  --line:#b8b8bc;
  --photo-light:#d6d6d8;
  --photo-mid:#9a9a9e;
  --photo-dark:#555558;
}
*{margin:0;padding:0;box-sizing:border-box}
html,body{width:1200px;height:5282px;overflow:hidden}
body{position:relative;background:var(--white);font-family:"Poppins",sans-serif;color:var(--ink)}
section,footer,header{position:absolute;left:0;width:1200px}
.abs{position:absolute}
.display{font-family:"Jost",sans-serif;font-weight:300}
.serif{font-family:"EB Garamond",serif}
.body-copy{font-size:11.5px;line-height:21px;color:var(--text);font-weight:300}
.pill{position:absolute;display:flex;align-items:center;height:38px;border-radius:19px;background:var(--charcoal);color:var(--white);font-size:13px;letter-spacing:.5px;padding:0 22px 0 4px;white-space:nowrap}
.pill .dot{width:32px;height:32px;border-radius:50%;background:var(--white);border:1px solid var(--line);margin-right:18px}
.photo{position:absolute}

/* hero */
.hero{top:0;height:712px;background:linear-gradient(180deg,#3a3a3c 0%,#5e5e60 40%,#7a7a7c 70%,#4a4a4c 100%)}
.brand{position:absolute;display:flex;align-items:center;gap:12px;color:var(--white);white-space:nowrap}
.brand .mark{width:46px;height:46px;border-radius:50%;border:1.5px solid rgba(255,255,255,.8)}
.brand .name{font-family:"Jost",sans-serif;font-weight:300;font-size:20px;letter-spacing:3px}
.menu{position:absolute;right:58px;top:30px;width:38px}
.menu span{display:block;height:2px;background:var(--white);margin-bottom:8px}
.hero h1{position:absolute;top:236px;width:100%;text-align:center;color:var(--white);font-size:72px;letter-spacing:1px}
.hero .tagline{position:absolute;top:332px;width:100%;text-align:center;color:var(--white);font-style:italic;font-size:18px;line-height:28px}

/* about */
.about{top:712px;height:560px}
.ring{position:absolute;left:157px;top:108px;width:370px;height:370px;border-radius:50%;border:8px dotted var(--ink)}
.about .eyebrow{left:662px;top:108px;font-size:17px}
.about h2{left:662px;top:140px;font-size:38px}

/* services */
.services{top:1272px;height:1332px}
.band{position:absolute;background:var(--band)}
.shape{border-radius:0 110px 0 110px}
.vlabel{position:absolute;writing-mode:vertical-rl;transform:rotate(180deg);font-family:"Jost",sans-serif;font-weight:300;font-size:27px;color:var(--ink);white-space:nowrap}

/* offerings */
.offer{top:2604px;height:537px;background:var(--charcoal)}
.offer-links{position:absolute;left:0;width:1200px;text-align:center;color:var(--white)}
.offer-links li{list-style:none;position:absolute;width:100%;font-family:"Jost",sans-serif;font-weight:300;font-size:38px}

/* process */
.process{top:3141px;height:502px;background:var(--mist)}
.process h2{top:80px;width:100%;text-align:center;font-size:37px}
.step{position:absolute;top:162px;width:250px;text-align:center}
.step .badge{margin:0 auto;width:134px;height:134px;border-radius:50%;border:3px dotted var(--charcoal);display:flex;align-items:center;justify-content:center}
.step .badge div{width:112px;height:112px;border-radius:50%;background:var(--charcoal);display:flex;align-items:center;justify-content:center}
.step h3{font-weight:400;font-size:18px;margin-top:40px}
.step p{font-size:10.5px;line-height:19px;color:var(--text);margin-top:10px;font-weight:300}

/* schedule */
.schedule{top:3643px;height:375px}
.schedule h2{top:68px;width:100%;text-align:center;font-size:36px;line-height:42px}
.schedule p{top:170px;width:100%;text-align:center}
.signup{position:absolute;left:330px;top:244px;width:539px;height:38px;border:1px solid var(--ink);border-radius:19px;font-size:11px;color:var(--text);padding:12px 16px}

/* blog */
.blog{top:4018px;height:482px}
.blog .shade{position:absolute;left:0;top:174px;width:1200px;height:308px;background:var(--mist)}
.blog h2{left:62px;top:58px;font-size:38px}
.card{position:absolute;top:0;width:262px}
.card .img{height:261px}
.card h3{font-size:17px;font-weight:500;line-height:25px;margin-top:22px}
.card p{font-size:10.5px;line-height:21px;color:var(--text);margin-top:8px;font-weight:300}

/* quote */
.quote{top:4500px;height:400px}
.quote blockquote{top:178px;width:100%;text-align:center;font-size:19px;line-height:30px;color:var(--ink)}
.quote cite{top:312px;width:100%;text-align:center;font-style:normal;font-size:11px;color:var(--line)}

/* footer */
.site-footer{top:4900px;height:382px;background:var(--charcoal);color:var(--white)}
.foot-nav{position:absolute;left:78px;top:44px;list-style:none;font-size:11px;line-height:21.5px}
.foot-nav li::before{content:"";display:inline-block;width:4px;height:4px;border-radius:50%;background:var(--white);margin:0 12px 2px -16px;vertical-align:middle}
.contact-list{position:absolute;right:58px;top:42px;text-align:right;font-size:11px;line-height:22px}
.contact-list .row{display:flex;align-items:center;justify-content:flex-end;gap:22px}
</style>
</head>
<body>

<header class="hero">
  <div class="photo" role="img" aria-label="Woman with open arms in a sunlit forest" style="inset:0;background:linear-gradient(180deg,rgba(30,30,30,.15),rgba(15,15,15,.35))"></div>
  <div class="brand" style="left:64px;top:18px"><span class="mark"></span><span class="name">THE QUIET MEADOW</span></div>
  <div class="menu"><span></span><span></span><span></span></div>
  <h1 class="display">THE QUIET MEADOW</h1>
  <p class="tagline">Virtual Consulting firm focused on Holistic Wellness and<br>Sustainable Living</p>
  <a class="pill" style="left:530px;top:414px;background:var(--charcoal-soft)"><span class="dot"></span>SIGN UP</a>
</header>

<section class="about">
  <div class="ring"></div>
  <div class="photo" role="img" aria-label="Portrait of the founder" style="left:188px;top:139px;width:308px;height:308px;border-radius:50%;background:radial-gradient(circle at 50% 45%,#c8c8ca,#6e6e72 70%,#e8e8e9 71%)"></div>
  <p class="abs eyebrow serif">About Us</p>
  <h2 class="abs display">The Quiet Meadow</h2>
  <p class="abs body-copy" style="left:665px;top:200px;width:400px">Lorem Ipsum has been the industry's standard dummy text ever since the 1500s, when an unknown printer took a galley of type and scrambled it to make a type specimen book. versions of Lorem Ipsum.</p>
  <p class="abs body-copy" style="left:665px;top:296px;width:400px">Lorem Ipsum has been the industry's standard dummy text ever since the 1500s, when an unknown printer took a galley of type and scrambled it to make a type specimen book. It has survived not only five centuries, but also the leap into electronic type setting, remaining essentially unchanged. It was popularised in the 1960s with the release of Letraset sheets.</p>
  <a class="pill" style="left:664px;top:444px"><span class="dot"></span>KNOW MORE</a>
</section>

<section class="services">
  <p class="abs serif" style="left:146px;top:142px;font-size:18px">What We Do</p>
  <h2 class="abs display" style="left:146px;top:172px;font-size:38px">Our Services</h2>
  <p class="abs body-copy" style="left:149px;top:232px;width:345px">Lorem Ipsum has been the industry's standard dummy text ever since the , when an unknown printer took a galley of type and scrambled it to make.</p>

  <div class="band" style="left:955px;top:132px;width:123px;height:482px"></div>
  <div class="photo shape" role="img" aria-label="Woman on a video call with a consultant" style="left:642px;top:71px;width:371px;height:508px;background:linear-gradient(135deg,#d8d8da,#9c9ca0 55%,#606064)"></div>
  <span class="vlabel" style="left:1030px;top:290px">Virtual Consulting</span>

  <div class="band" style="left:121px;top:425px;width:123px;height:482px"></div>
  <div class="photo shape" role="img" aria-label="Woman practising yoga in a green tea field" style="left:187px;top:466px;width:371px;height:509px;background:linear-gradient(160deg,#bdbdbf,#8a8a8d 55%,#505053)"></div>
  <span class="vlabel" style="left:138px;top:570px">Holistic Wellness</span>

  <div class="band" style="left:955px;top:770px;width:123px;height:482px"></div>
  <div class="photo shape" role="img" aria-label="Girl hugging a tree trunk" style="left:642px;top:708px;width:371px;height:509px;background:linear-gradient(150deg,#454548,#6a6a6d 50%,#b4b4b7)"></div>
  <span class="vlabel" style="left:1030px;top:922px">Sustainable Living</span>
</section>

<section class="offer">
  <div class="photo" role="img" aria-label="Studio microphone in soft light" style="left:117px;top:225px;width:238px;height:238px;background:linear-gradient(135deg,#c9c9cc,#8e8e92 60%,#e2e2e4)"></div>
  <div class="photo" role="img" aria-label="Leaves, wooden spoon and natural cosmetics" style="left:861px;top:75px;width:209px;height:222px;background:linear-gradient(150deg,#e6e6e7,#b8b8ba 50%,#646467)"></div>
  <ul class="offer-links">
    <li style="top:70px">Shop Online</li>
    <li style="top:166px">Podcast</li>
    <li style="top:240px">Online Series</li>
    <li style="top:308px">Coaching</li>
  </ul>
  <svg class="abs" style="left:574px;top:414px" width="54" height="16" viewBox="0 0 54 16"><polyline points="2,2 27,14 52,2" fill="none" stroke="#fff" stroke-width="1.5"/></svg>
</section>

<section class="process">
  <h2 class="abs display">Our Process</h2>
  <svg class="abs" style="left:0;top:0" width="1200" height="502">
    <g stroke="#b8b8bc" stroke-width="1.3" fill="none">
      <line x1="269" y1="229" x2="377" y2="229"/><polyline points="371,224 377,229 371,234"/>
      <line x1="547" y1="229" x2="656" y2="229"/><polyline points="650,224 656,229 650,234"/>
      <line x1="826" y1="229" x2="935" y2="229"/><polyline points="929,224 935,229 929,234"/>
    </g>
  </svg>
  <div class="step" style="left:60px"><div class="badge"><div>
    <svg width="48" height="44" viewBox="0 0 48 44" fill="none" stroke="#fff" stroke-width="2"><circle cx="14" cy="22" r="7"/><path d="M2 42c0-8 6-12 12-12s12 4 12 12"/><rect x="24" y="2" width="22" height="16" rx="2"/></svg>
  </div></div><h3>Understand</h3><p>Always remember in the jungle there's a lot of them in there, after you overcome them, you will make it to paradise.</p></div>
  <div class="step" style="left:336px"><div class="badge"><div>
    <svg width="46" height="46" viewBox="0 0 46 46" fill="none" stroke="#fff" stroke-width="2"><circle cx="23" cy="20" r="8"/><path d="M6 42c2-9 9-13 17-13s15 4 17 13"/><path d="M34 4v8M30 8h8"/></svg>
  </div></div><h3>Imagine</h3><p>You see the hedges, how I got it shaped up? It's important to shape up your hedges, it's like getting a haircut, stay fresh.</p></div>
  <div class="step" style="left:613px"><div class="badge"><div>
    <svg width="48" height="48" viewBox="0 0 48 48" fill="none" stroke="#fff" stroke-width="2"><circle cx="24" cy="24" r="21"/><path d="M24 13v22M13 24h22"/></svg>
  </div></div><h3>Create</h3><p>We don't see them, we will never see them. To be successful you've got to work hard, to make history, simple, you've got to make it.</p></div>
  <div class="step" style="left:890px"><div class="badge"><div>
    <svg width="48" height="44" viewBox="0 0 48 44" fill="none" stroke="#fff" stroke-width="2"><rect x="3" y="3" width="42" height="30" rx="3"/><path d="M16 42h16M24 33v9"/><rect x="14" y="12" width="10" height="10"/><rect x="24" y="18" width="10" height="10"/></svg>
  </div></div><h3>Build</h3><p>Look at the sunset. Surround yourself with angels, positive energy, beautiful people, beautiful souls, clean heart, angel.</p></div>
</section>

<section class="schedule">
  <h2 class="abs display">We Make Scheduling For You<br>Easier Than Ever</h2>
  <p class="abs body-copy" style="font-size:12.5px;line-height:23px">Planwise is your scheduling automation platform for eliminating the hassle of<br>back-and-forth emails for finding the perfect time — and so much more</p>
  <div class="signup">Enter Email *</div>
  <a class="pill" style="left:734px;top:244px"><span class="dot"></span>SIGN UP</a>
</section>

<section class="blog">
  <div class="shade"></div>
  <h2 class="abs display">Latest Blog</h2>
  <svg class="abs" style="left:62px;top:136px" width="46" height="28" viewBox="0 0 46 28" fill="none" stroke="#1e1e20" stroke-width="1.5"><polyline points="14,2 4,14 14,26"/><polyline points="32,2 42,14 32,26"/></svg>
  <article class="card" style="left:377px"><div class="img" role="img" aria-label="Hands holding a tablet beside breakfast bowls" style="background:linear-gradient(140deg,#d8d8d9,#a6a6a8 55%,#59595c)"></div><h3>Executive &amp;<br>Individual coaching</h3><p>Lorem Ipsum has been the industry's thisis standard dummy text ever since the 1500s, when an unknown printer took.</p></article>
  <article class="card" style="left:664px"><div class="img" role="img" aria-label="Stacked stones and bamboo in raked sand" style="background:linear-gradient(160deg,#e6e6e7,#c6c6c8 60%,#858588)"></div><h3>The Quiet Meadow</h3><p>Lorem Ipsum has been the industry's this is standard dummy text ever since the 1500s, when an unknown printer took.</p></article>
  <article class="card" style="left:951px"><div class="img" role="img" aria-label="Woman seated in a bright studio with a camera" style="background:linear-gradient(140deg,#ececed,#c0c0c2 55%,#48484b)"></div><h3>Executive &amp;<br>Individual coaching</h3><p>Lorem Ipsum has been the industry's this is standard dummy text ever since the 1500s, when an unknown printer took.</p></article>
</section>

<section class="quote">
  <div class="photo" role="img" aria-label="Portrait of the founder" style="left:556px;top:70px;width:90px;height:90px;border-radius:50%;border:3px solid var(--mist);background:linear-gradient(160deg,#b4b4b7,#808083 60%,#38383b)"></div>
  <blockquote class="abs serif">“ Doing the work to help ourselves to see and know our own worth,<br>our power and our purpose enables us to see and know others more<br>purposefully and fully as humans. ”</blockquote>
  <cite class="abs">— Gina Poslund, Founder of the Quiet Meadow</cite>
</section>

<footer class="site-footer">
  <ul class="foot-nav"><li>Home</li><li>Online shop</li><li>Blog</li><li>Services</li><li>About</li><li>Contact</li></ul>
  <div class="brand" style="left:470px;top:58px"><span class="mark"></span><span class="name" style="font-size:22px">THE QUIET MEADOW</span></div>
  <p class="abs display" style="top:142px;width:100%;text-align:center;font-size:19px">Let's Work together.</p>
  <a class="pill" style="left:513px;top:181px;background:transparent;border:1px solid #fff;font-size:12px"><span class="dot"></span>CONTACT US</a>
  <div class="abs" style="left:531px;top:275px;display:flex;gap:6px" role="img" aria-label="Social media links">
    <span style="width:40px;height:40px;border-radius:50%;background:#e0e0e2"></span>
    <span style="width:40px;height:40px;border-radius:50%;background:#e0e0e2"></span>
    <span style="width:40px;height:40px;border-radius:50%;background:#e0e0e2"></span>
  </div>
  <p class="abs" style="top:341px;width:100%;text-align:center;font-size:10px">©THE QUIET MEADOW - 2022 All rights reserved.</p>
  <div class="contact-list">
    <div class="row"><span>+1 555 014 2290</span><svg width="18" height="18" viewBox="0 0 24 24" fill="#fff"><path d="M6.6 10.8a15 15 0 0 0 6.6 6.6l2.2-2.2a1 1 0 0 1 1-.25 11 11 0 0 0 3.6.6 1 1 0 0 1 1 1V20a1 1 0 0 1-1 1A17 17 0 0 1 3 4a1 1 0 0 1 1-1h3.5a1 1 0 0 1 1 1 11 11 0 0 0 .6 3.6 1 1 0 0 1-.25 1z"/></svg></div>
    <div class="row" style="margin-top:8px"><span>info@thequietmeadowhub.example</span><svg width="18" height="14" viewBox="0 0 18 14" fill="none" stroke="#fff" stroke-width="1.6"><rect x="1" y="1" width="16" height="12" rx="1"/><polyline points="1,1 9,8 17,1"/></svg></div>
    <div class="row" style="margin-top:18px;align-items:flex-start"><span>The Meadow House<br>101 Lorem ipsum simple<br>text print type industry</span><svg width="16" height="22" viewBox="0 0 16 22" fill="none" stroke="#fff" stroke-width="1.6" style="margin-top:16px"><path d="M8 21s7-8 7-13A7 7 0 0 0 1 8c0 5 7 13 7 13z"/><circle cx="8" cy="8" r="2.5"/></svg></div>
  </div>
</footer>

</body>
</html>
```